Web Design For Calloway Pool Service

We are working with a company that wants a website for their pool service. Some sites to use for content/competitors and inspiration:
https://sacramento.brimwaterpools.example/builder/newbuild/repair/ppc
https://coralbaypoolcareandmore.example/
https://lumoxpoolservice.example/
https://www.halvorsenspoolresurfacing.example/pool-renovation-ga/
Thank you for taking the time to consider designing a website for us. We are web developers based in Stockton, CA, USA. Most of our projects go through the same process. Understanding this process may help you win a project with us. We custom-code all of our websites in-house. We don’t have any requirements as to what tools you use for your design, but we prefer Figma files. For any design that we label as four-stars, we send it to the client for review. The client picks the final design they want us to use. Once we complete this process, we will continue to show additional clients all the four-star sites and purchase them later. Your designs will have multiple chances to sell. For better chances of success, we ask that you follow these guidelines.
IMAGES:
If you use any images or icons in the design, we ask that you have a link to the asset so we can purchase the image/icon. Most of the designs we submit do not have the customer’s images on them unless they have some great images. Be creative; show us the feeling you are trying to portray with your image choices. Use any royalty-free site you choose. We subscribe to Adobe and mainly use their images, but we can purchase images outside of Adobe. PLEASE NOTE: we will not submit designs to clients with watermarks on the images.
FONTS:
We ask that you identify the fonts used in the design. This can be done in a message if you want. We typically use Google Fonts and Adobe Fonts.
CONTENT:
We're always open to different content and ideas. We often submit designs with stock images so the client can see our vision. We typically take pictures after the website launch to use their images with our vision. Lorem Ipsum is fine for paragraphs, but we ask that you write the headers in correct English. We want to be able to show the vision and identify the sections of the website.
INSPIRATION:
We typically add a couple of links in the brief of websites we like to help you get started in your design.
REVISIONS:
We do not often ask for revisions of the designs unless we see something in the design that may not appeal to the client. If there are slight changes that we want to make, we do that in the development process.
FEEDBACK:
We rarely give feedback on designs during the design process. We are working on many website projects and do not have the time to provide feedback. We usually respond if your request is well thought out and asks specific questions, but a note asking “feedback, please” usually goes unanswered.

```html
<!DOCTYPE html>
<html lang="en">
<head>
<meta charset="utf-8">
<title>Calloway Pool Service</title>
<link href="https://fonts.googleapis.com/css2?family=Libre+Baskerville:wght@400;700&family=Lato:wght@400;700;900&display=swap" rel="stylesheet">
<style>
:root{
  --navy:#1b3f7d;
  --navy-dark:#163466;
  --blue:#2a9df4;
  --ink:#1d3557;
  --text:#3c4656;
  --muted:#6b7280;
  --soft:#f4f5f8;
  --line:#e3e7ee;
  --white:#ffffff;
  --star:#f07f1a;
}
*{box-sizing:border-box;margin:0;padding:0}
html,body{width:1200px;height:4841px;overflow:hidden}
body{font-family:"Lato",Arial,sans-serif;color:var(--text);background:var(--white)}
.page{position:relative;width:1200px;height:4841px;overflow:hidden}
.abs{position:absolute}
.serif{font-family:"Libre Baskerville",Georgia,serif;color:var(--ink);font-weight:700}
.label{position:absolute;font-size:11px;font-weight:700;letter-spacing:.5px;color:var(--blue);display:flex;align-items:center;gap:12px}
.label::after{content:"";width:50px;height:2px;background:var(--blue)}
.label.center::before{content:"";width:50px;height:2px;background:var(--blue)}
.photo{position:absolute}

/* header */
.topbar{top:0;left:0;width:1200px;height:34px;background:#efefef}
.topbar .welcome{position:absolute;left:394px;top:10px;font-size:13px;color:#333;letter-spacing:.5px}
.topbar .divider{position:absolute;left:592px;top:6px;width:1px;height:22px;background:#bbb}
.topbar .mail{position:absolute;left:626px;top:6px;display:flex;align-items:center;gap:8px;font-size:12px;color:#333}
.navbar{top:34px;left:0;width:1200px;height:52px;background:var(--white)}
.brand-badge{position:absolute;left:160px;top:0;width:150px;height:94px;background:var(--white);border-radius:50%;box-shadow:0 2px 6px rgba(0,0,0,.12);display:flex;align-items:center;justify-content:center;gap:6px;z-index:3}
.brand-badge .dot{width:12px;height:12px;border-radius:50%;background:var(--blue)}
.brand-badge span{font-size:13px;font-weight:700;color:var(--blue);line-height:1.1;text-align:left}
.nav{position:absolute;top:55px;font-size:13px;color:#222;font-weight:700}
.nav.active{color:var(--blue)}
.callbox{position:absolute;left:888px;top:0;width:169px;height:86px;background:var(--navy);color:var(--white);padding:20px 0 0 14px;z-index:3}
.callbox small{display:block;font-size:14px}
.callbox strong{display:block;font-size:19px;margin-top:4px;font-weight:700;white-space:nowrap}
.callicon{position:absolute;left:857px;top:26px;width:36px;height:36px;border-radius:50%;background:var(--white);border:2px solid var(--navy);display:flex;align-items:center;justify-content:center;z-index:4}

/* hero */
.hero{top:86px;left:0;width:1200px;height:778px;background:linear-gradient(100deg,#1f3134 0%,#3b4a44 35%,#6d5a44 60%,#3e3528 100%)}
.hero-card{position:absolute;left:77px;top:272px;width:503px;height:359px;background:var(--white);padding:52px 0 0 45px}
.hero-card::before{content:"";position:absolute;left:0;top:56px;width:7px;height:112px;background:var(--blue)}
.hero-card h1{font-size:54px;line-height:66px;font-family:"Libre Baskerville",Georgia,serif;color:var(--ink)}
.hero-card p{margin-top:22px;font-size:11.5px;line-height:21px;color:var(--muted);width:410px}
.btn{display:inline-flex;align-items:center;justify-content:center;background:var(--blue);color:var(--white);font-weight:700;font-size:11px;border-radius:3px}
.hero-card .btn{margin-top:28px;width:133px;height:37px}
.wave{left:0;top:760px}

/* about */
.about-text{left:624px;top:997px;width:440px}
.about-text h2{position:absolute;top:34px;font-size:40px;line-height:60px;width:480px}
.about-text p{position:absolute;font-size:13px;line-height:24px;color:var(--text);width:440px}
.about-text .btn{position:absolute;top:348px;width:169px;height:47px;font-size:13px}

/* features */
.features{left:92px;top:1534px;width:1010px;height:212px;background:var(--white);border-radius:0 0 90px 90px;box-shadow:0 10px 30px rgba(20,40,80,.10)}
.feature{position:absolute;top:40px;width:300px}
.feature .ico{position:absolute;left:0;top:0;width:62px;height:62px;border-radius:50%;border:2px solid var(--navy);display:flex;align-items:center;justify-content:center}
.feature h3{position:absolute;left:80px;top:10px;font-size:21px;font-family:"Libre Baskerville",Georgia,serif;color:var(--ink);font-weight:700}
.feature h4{position:absolute;left:82px;top:42px;font-size:16px;font-weight:400;color:var(--ink)}
.feature p{position:absolute;left:80px;top:70px;width:200px;font-size:12.5px;line-height:24px;color:var(--text)}

/* services */
.arrow-btn{position:absolute;top:1870px;width:45px;height:60px;background:var(--white);box-shadow:0 2px 10px rgba(0,0,0,.12);display:flex;align-items:center;justify-content:center}
.svc-card{position:absolute;top:2150px;width:271px;height:198px;background:var(--white);box-shadow:0 6px 18px rgba(20,40,80,.10);padding:20px 0 0 30px}
.svc-card h3{font-size:19px;font-family:"Libre Baskerville",Georgia,serif;color:var(--ink)}
.svc-card p{margin-top:12px;font-size:12.5px;line-height:24px;width:218px;color:var(--text)}
.svc-card a{display:block;margin-top:12px;font-weight:700;font-size:15px;color:var(--blue);text-decoration:none}
.svc-card.dark{background:var(--navy)}
.svc-card.dark h3,.svc-card.dark p,.svc-card.dark a{color:var(--white)}
.outline-btn{position:absolute;left:500px;top:2391px;width:191px;height:45px;border:2px solid var(--blue);border-radius:24px;color:var(--blue);font-weight:700;font-size:14px;display:flex;align-items:center;justify-content:center}

/* soft band */
.soft-band{left:0;top:2507px;width:1200px;height:1890px;background:var(--soft)}

/* why choose */
.why-item{position:absolute}
.why-item h4{position:absolute;left:32px;top:0;font-size:15px;color:var(--navy);white-space:nowrap}
.why-item p{position:absolute;left:36px;top:28px;width:200px;font-size:13px;line-height:23px;color:var(--text)}

/* testimonials */
.t-card{position:absolute;top:3390px;width:320px;height:263px;background:var(--white);text-align:center}
.t-avatar{position:absolute;left:126px;top:-34px;width:68px;height:68px;border-radius:50%;border:3px solid var(--white);box-shadow:0 2px 8px rgba(0,0,0,.15)}
.t-stars{position:absolute;top:66px;width:100%;color:var(--star);font-size:20px;letter-spacing:8px}
.t-card p{position:absolute;left:45px;top:110px;width:230px;font-size:13px;line-height:24px;color:var(--muted)}
.t-quote{position:absolute;left:125px;top:235px;width:70px;height:46px;background:var(--navy);border-radius:35px 35px 0 0;display:flex;align-items:center;justify-content:center;color:var(--white);font-family:Georgia,serif;font-size:30px;font-weight:700;padding-top:10px}
.t-name{position:absolute;top:3690px;width:320px;text-align:center;font-weight:700;font-size:18px;color:#333}
.t-place{position:absolute;top:3720px;width:320px;text-align:center;font-size:13px;color:var(--muted)}

/* contact */
.contact-frame{left:648px;top:3981px;width:462px;height:470px;background:var(--white);border-radius:14px;padding:7px}
.contact-inner{width:100%;height:100%;background:var(--navy);border-radius:10px;position:relative;text-align:center}
.contact-inner h2{padding-top:38px;font-size:27px;color:var(--white);font-weight:700}
.contact-inner p{margin:8px auto 0;width:370px;font-size:10.5px;line-height:17px;color:#dce4f2}
.field{position:absolute;left:30px;width:393px;height:44px;background:#5a7cb0;border-radius:3px;color:var(--white);font-size:10px;text-align:left;padding:15px 0 0 28px;letter-spacing:.3px}
.submit{position:absolute;left:30px;top:378px;width:393px;height:45px;background:var(--white);border-radius:3px}

/* footer */
.f-head{position:absolute;top:4555px;font-size:14px;color:var(--blue)}
.f-head::after{content:"";display:block;width:118px;height:1px;background:#c9d3e0;margin-top:9px}
.f-link{position:absolute;font-size:14px;color:#444}
.social{position:absolute;top:4670px;width:26px;height:26px;border-radius:50%;background:#e6e8ec}
</style>
</head>
<body>
<div class="page">

  <!-- header -->
  <div class="abs topbar">
    <span class="welcome">WELCOME</span>
    <span class="divider"></span>
    <span class="mail">
      <svg width="24" height="24" viewBox="0 0 24 24"><circle cx="12" cy="12" r="11" fill="none" stroke="#1b3f7d" stroke-width="1.5"/><rect x="6.5" y="8" width="11" height="8" fill="none" stroke="#1b3f7d" stroke-width="1.4"/><path d="M6.5 8l5.5 4.5L17.5 8" fill="none" stroke="#1b3f7d" stroke-width="1.4"/></svg>
      hello@calloway.example
    </span>
  </div>
  <div class="abs navbar"></div>
  <div class="brand-badge"><i class="dot"></i><span>CALLOWAY<br>POOL SERVICE</span></div>
  <span class="nav active" style="left:336px">HOME</span>
  <span class="nav" style="left:424px">About Us</span>
  <span class="nav" style="left:518px">Services</span>
  <span class="nav" style="left:610px">Gallery</span>
  <span class="nav" style="left:710px">Contact Us</span>
  <div class="callicon">
    <svg width="18" height="18" viewBox="0 0 24 24"><path d="M6.6 10.8a15 15 0 006.6 6.6l2.2-2.2a1 1 0 011-.25 11.4 11.4 0 003.6.57 1 1 0 011 1V20a1 1 0 01-1 1A17 17 0 013 4a1 1 0 011-1h3.5a1 1 0 011 1c0 1.25.2 2.45.57 3.57a1 1 0 01-.25 1z" fill="#1b3f7d"/></svg>
  </div>
  <div class="callbox"><small>Call us today at</small><strong>(555) 014-2287</strong></div>

  <!-- hero -->
  <div class="photo hero" role="img" aria-label="Woman relaxing at the edge of a pool at dusk"></div>
  <svg class="abs wave" width="1200" height="110" viewBox="0 0 1200 110">
    <path d="M0 60 C220 0 420 20 640 50 C860 80 1040 60 1200 0 V110 H0Z" fill="#ffffff"/>
    <path d="M0 62 C200 10 420 40 620 62 C820 84 1020 70 1200 10 V30 C1020 84 820 100 620 80 C420 60 200 40 0 78Z" fill="#1b3f7d"/>
    <path d="M0 50 C200 0 420 25 640 45 C860 65 1040 45 1200 0 V8 C1040 52 860 72 640 54 C420 36 200 12 0 60Z" fill="#2a9df4"/>
  </svg>
  <div class="hero-card">
    <h1>Dive into Your Dream Pool</h1>
    <p>Lorem ipsum dolor sit amet, consectetur adipiscing elit, sed do eiusmo d tempor incididunt ut labore et dolore orem ipsum dolor</p>
    <span class="btn">Discover More</span>
  </div>

  <!-- about -->
  <div class="photo" role="img" aria-label="Woman floating on a pink inflatable in a blue pool" style="left:103px;top:971px;width:305px;height:335px;background:linear-gradient(135deg,#3aa3d8,#1f7fc0 60%,#e27aa6);border-radius:90px 0 0 90px"></div>
  <div class="photo" role="img" aria-label="Backyard pool beside a modern house" style="left:430px;top:993px;width:117px;height:121px;background:linear-gradient(160deg,#d9e3ea,#7a6a55 50%,#2e8fc9);border-radius:0 0 0 60px"></div>
  <div class="photo" role="img" aria-label="Pool deck with cleaning equipment" style="left:267px;top:1132px;width:306px;height:314px;background:linear-gradient(120deg,#39a6e0 0%,#2487c9 45%,#c9c9c4 55%,#8d8f92 100%);border-radius:0 0 90px 90px"></div>
  <div class="abs" style="left:240px;top:1216px;width:96px;height:96px;border-radius:50%;background:var(--navy);border:4px solid #fff"></div>

  <div class="abs about-text">
    <span class="label" style="top:0;left:0">ABOUT US</span>
    <h2 class="serif">Crafting Aquatic Masterpieces</h2>
    <p style="top:160px">Lorem ipsum dolor sit amet, consectetur adipiscing elit, sed do eiusmo empor incididunt ut abore et dolore magna aliqua. Ut enim ad minim iam, quis nostrud exercitation ullamco</p>
    <p style="top:240px">Lorem ipsum dolor sit amet, consectetur adipiscing elit, sed do eiusmo empor incididunt ut abore et dolore magna aliqua. Ut enim ad minim iam, quis nostrud exercitation ullamco</p>
    <span class="btn">Contact Us</span>
  </div>

  <!-- features -->
  <div class="abs features">
    <div class="feature" style="left:56px">
      <div class="ico"><svg width="30" height="30" viewBox="0 0 24 24" fill="none" stroke="#1b3f7d" stroke-width="1.5"><circle cx="12" cy="12" r="3.5"/><path d="M12 2v3M12 19v3M2 12h3M19 12h3M4.9 4.9l2.1 2.1M17 17l2.1 2.1M4.9 19.1L7 17M17 7l2.1-2.1"/></svg></div>
      <h3>Expertise</h3><h4>Lorem Ipsum</h4>
      <p>Lorem ipsum dolor sit amet, empor incididunt ut abore et iam, quis nostrud exe</p>
    </div>
    <div class="feature" style="left:364px">
      <div class="ico"><svg width="30" height="30" viewBox="0 0 24 24" fill="none" stroke="#1b3f7d" stroke-width="1.5"><circle cx="11" cy="11" r="7"/><circle cx="11" cy="11" r="3"/><circle cx="17.5" cy="17.5" r="3"/></svg></div>
      <h3>Professional</h3><h4>Lorem Ipsum</h4>
      <p>Lorem ipsum dolor sit amet, empor incididunt ut abore et iam, quis nostrud exe</p>
    </div>
    <div class="feature" style="left:674px">
      <div class="ico"><svg width="30" height="30" viewBox="0 0 24 24" fill="none" stroke="#1b3f7d" stroke-width="1.5"><circle cx="12" cy="8" r="4"/><path d="M4 21c0-4.4 3.6-7 8-7s8 2.6 8 7z"/></svg></div>
      <h3>Experienced</h3><h4>Lorem Ipsum</h4>
      <p>Lorem ipsum dolor sit amet, empor incididunt ut abore et iam, quis nostrud exe</p>
    </div>
  </div>

  <!-- services -->
  <span class="label" style="left:96px;top:1853px">BENEFITS</span>
  <h2 class="abs serif" style="left:94px;top:1893px;font-size:40px">Services We Provide</h2>
  <div class="arrow-btn" style="left:1005px"><svg width="14" height="14" viewBox="0 0 14 14"><path d="M9 2L4 7l5 5" fill="none" stroke="#222" stroke-width="2"/></svg></div>
  <div class="arrow-btn" style="left:1057px"><svg width="14" height="14" viewBox="0 0 14 14"><path d="M5 2l5 5-5 5" fill="none" stroke="#222" stroke-width="2"/></svg></div>

  <div class="photo" role="img" aria-label="Technician repairing pool tiles" style="left:90px;top:1974px;width:321px;height:233px;background:linear-gradient(120deg,#1e6fa8,#4aa7d6 50%,#c7dbe6)"></div>
  <div class="photo" role="img" aria-label="Construction crew in hard hats on a pool site" style="left:438px;top:1974px;width:321px;height:233px;background:linear-gradient(120deg,#8fa7b8,#d8dde0 50%,#b7c16a)"></div>
  <div class="photo" role="img" aria-label="Family enjoying a clean outdoor pool" style="left:785px;top:1974px;width:321px;height:233px;background:linear-gradient(160deg,#6f8a5a,#3fa7c9 55%,#1f86c0)"></div>

  <div class="svc-card" style="left:120px">
    <h3>Pool Repair</h3>
    <p>Lorem ipsum dolor sit amet, con sectetur Lorem ipsum dolor sit am et, consectetur Lorem ipsum dolor</p>
    <a>Read More</a>
  </div>
  <div class="svc-card dark" style="left:458px">
    <h3>Pool Construction</h3>
    <p>Lorem ipsum dolor sit amet, con sectetur Lorem ipsum dolor sit am et, consectetur Lorem ipsum dolor</p>
    <a>Read More</a>
  </div>
  <div class="svc-card" style="left:806px">
    <h3>Pool Cleaning</h3>
    <p>Lorem ipsum dolor sit amet, con sectetur Lorem ipsum dolor sit am et, consectetur Lorem ipsum dolor</p>
    <a>Read More</a>
  </div>
  <div class="outline-btn">MORE SERVICES</div>

  <!-- soft band -->
  <div class="abs soft-band"></div>

  <!-- why choose -->
  <span class="label" style="left:94px;top:2612px">WHY CHOOSE US</span>
  <h2 class="abs serif" style="left:92px;top:2648px;font-size:40px;line-height:60px">Why Choose<br>Us</h2>
  <p class="abs" style="left:94px;top:2778px;width:440px;font-size:13px;line-height:24px">Lorem ipsum dolor sit amet, consectetur adipiscing elit, sed do eiusmo empor incididunt ut abore et dolore magna aliqua. Ut enim ad minim iam, quis nostrud exercitation ullamco</p>

  <div class="why-item" style="left:108px;top:2882px">
    <svg width="26" height="26" viewBox="0 0 24 24" fill="none" stroke="#2a9df4" stroke-width="1.5"><path d="M4 14a8 8 0 1116 0"/><path d="M12 14l3-4"/><circle cx="12" cy="14" r="1.2" fill="#2a9df4"/></svg>
    <h4 style="top:3px">Quality Assurance</h4>
    <p>Lorem ipsum dolor sit amet, consectetur adipiscing</p>
  </div>
  <div class="why-item" style="left:372px;top:2878px">
    <svg width="26" height="26" viewBox="0 0 24 24" fill="none" stroke="#2a9df4" stroke-width="1.5"><path d="M12 3l2.6 5.3 5.9.9-4.3 4.1 1 5.8L12 16.4 6.8 19.1l1-5.8L3.5 9.2l5.9-.9z"/></svg>
    <h4 style="top:7px">Proven Record</h4>
    <p style="top:32px">Lorem ipsum dolor sit amet, consectetur adipiscing</p>
  </div>
  <div class="why-item" style="left:108px;top:2978px">
    <svg width="26" height="26" viewBox="0 0 24 24" fill="none" stroke="#2a9df4" stroke-width="1.5"><path d="M4 20h16M7 20l5-14 5 14M9 14h6"/></svg>
    <h4 style="top:3px">Trusted Professionals</h4>
    <p>Lorem ipsum dolor sit amet, consectetur adipiscing</p>
  </div>
  <div class="why-item" style="left:372px;top:2978px">
    <svg width="26" height="26" viewBox="0 0 24 24" fill="none" stroke="#2a9df4" stroke-width="1.5"><circle cx="8" cy="8" r="3"/><circle cx="16" cy="8" r="3"/><path d="M2 19c0-3 2.7-5 6-5s6 2 6 5M10 19c0-3 2.7-5 6-5s6 2 6 5"/></svg>
    <h4 style="top:3px">Comprehensive Services</h4>
    <p>Lorem ipsum dolor sit amet, consectetur adipiscing</p>
  </div>

  <svg class="abs" style="left:636px;top:2610px" width="480" height="480" viewBox="0 0 480 480">
    <path d="M240 8 A232 232 0 0 1 472 240" fill="none" stroke="#2a9df4" stroke-width="8"/>
    <path d="M8 240 A232 232 0 0 1 240 8" fill="none" stroke="#2a9df4" stroke-width="3"/>
    <path d="M240 472 A232 232 0 0 1 8 240" fill="none" stroke="#1b3f7d" stroke-width="6"/>
  </svg>
  <div class="photo" role="img" aria-label="Man sitting at the edge of a blue pool, seen from above" style="left:656px;top:2632px;width:436px;height:436px;border-radius:50%;background:linear-gradient(135deg,#f1ece3 0%,#e4ddd0 32%,#2f8fd0 40%,#1c6fb2 100%)"></div>

  <!-- testimonials -->
  <span class="label center" style="left:497px;top:3222px">TESTIMONIALS</span>
  <h2 class="abs serif" style="left:0;top:3256px;width:1200px;text-align:center;font-size:40px">What Clients are Saying</h2>

  <div class="t-card" style="left:90px">
    <div class="t-avatar" role="img" aria-label="Client portrait" style="background:linear-gradient(160deg,#c8ced6,#4b5563)"></div>
    <div class="t-stars">★★★★★</div>
    <p>Lorem ipsum dolor sit amet, consectetur adipiscing elit, sed do eiusmod tempor incididunt ut labore et dolore</p>
    <div class="t-quote">“</div>
  </div>
  <div class="t-card" style="left:438px">
    <div class="t-avatar" role="img" aria-label="Client portrait" style="background:linear-gradient(160deg,#e8e6e1,#3b3b3b)"></div>
    <div class="t-stars">★★★★★</div>
    <p>Lorem ipsum dolor sit amet, consectetur adipiscing elit, sed do eiusmod tempor incididunt ut labore et dolore</p>
    <div class="t-quote">“</div>
  </div>
  <div class="t-card" style="left:787px">
    <div class="t-avatar" role="img" aria-label="Client portrait" style="background:linear-gradient(160deg,#d4d9de,#5e6670)"></div>
    <div class="t-stars">★★★★★</div>
    <p>Lorem ipsum dolor sit amet, consectetur adipiscing elit, sed do eiusmod tempor incididunt ut labore et dolore</p>
    <div class="t-quote">“</div>
  </div>
  <div class="t-name" style="left:90px">Dorian Welles</div><div class="t-place" style="left:90px">Los Angeles</div>
  <div class="t-name" style="left:438px">Dorian Welles</div><div class="t-place" style="left:438px">Australia</div>
  <div class="t-name" style="left:787px">Dorian Welles</div><div class="t-place" style="left:787px">Australia</div>

  <!-- contact -->
  <div class="photo" role="img" aria-label="Bright poolside living space" style="left:0;top:3897px;width:1200px;height:500px;background:linear-gradient(100deg,#6f7b86 0%,#a8a39a 25%,#e9e4da 38%,#9b9690 55%,#5d6d7c 80%,#4a6f8e 100%)"></div>
  <div class="photo" role="img" aria-label="Woman in a white blouse holding a tablet" style="left:180px;top:3775px;width:320px;height:622px;background:linear-gradient(180deg,#7a5a40 0%,#ece8e1 25%,#e5dfd5 70%,#b99d7e 100%);border-radius:140px 140px 0 0"></div>
  <div class="abs contact-frame">
    <div class="contact-inner">
      <h2>Connect With Us</h2>
      <p>Lorem ipsum dolor sit amet, consectetur adipiscing elit, sed do eius mod tempor incididunt ut labore et...</p>
      <div class="field" style="top:130px">NAME</div>
      <div class="field" style="top:204px">E-MAIL</div>
      <div class="field" style="top:279px">MESSAGE</div>
      <div class="submit"></div>
    </div>
  </div>

  <!-- footer -->
  <div class="abs" style="left:113px;top:4590px;display:flex;align-items:center;gap:8px">
    <i style="width:14px;height:14px;border-radius:50%;background:var(--blue)"></i>
    <span style="font-size:20px;font-weight:700;color:var(--blue);line-height:1.1">CALLOWAY<br>POOL SERVICE</span>
  </div>
  <span class="abs" style="left:113px;top:4674px;font-size:14px;font-weight:700;color:#333">Follow Us</span>
  <span class="social" style="left:195px"></span>
  <span class="social" style="left:232px"></span>
  <span class="social" style="left:269px"></span>

  <div class="f-head" style="left:364px">Quick Links</div>
  <span class="f-link" style="left:364px;top:4604px">Home</span>
  <span class="f-link" style="left:364px;top:4636px">About us</span>
  <span class="f-link" style="left:364px;top:4668px">Services</span>
  <span class="f-link" style="left:364px;top:4700px">Contact us</span>

  <div class="f-head" style="left:586px">Contact</div>
  <svg class="abs" style="left:602px;top:4604px" width="18" height="18" viewBox="0 0 24 24" fill="none" stroke="#2a9df4" stroke-width="1.6"><path d="M12 22s7-7 7-12a7 7 0 00-14 0c0 5 7 12 7 12z"/><circle cx="12" cy="10" r="2.5"/></svg>
  <span class="f-link" style="left:635px;top:4604px;line-height:22px">88 Harbor Lane<br>Suite 210</span>
  <svg class="abs" style="left:602px;top:4663px" width="18" height="18" viewBox="0 0 24 24" fill="none" stroke="#2a9df4" stroke-width="1.6"><path d="M6.6 10.8a15 15 0 006.6 6.6l2.2-2.2 4.6 1.6V20A17 17 0 013 4h3.8l1.6 4.6z"/></svg>
  <span class="f-link" style="left:635px;top:4662px">1-800-555-0199</span>
  <svg class="abs" style="left:602px;top:4701px" width="18" height="18" viewBox="0 0 24 24" fill="none" stroke="#2a9df4" stroke-width="1.6"><rect x="3" y="6" width="18" height="12"/><path d="M3 6l9 7 9-7"/></svg>
  <span class="f-link" style="left:635px;top:4700px">hello@calloway.example</span>

  <div class="f-head" style="left:860px">Join our Newsletter</div>
  <span class="f-link" style="left:860px;top:4604px;width:230px;line-height:19px;font-size:13.5px">Sign up for our newsletter to know the latest from us</span>
  <div class="abs" style="left:860px;top:4658px;width:145px;height:33px;border:1px solid var(--line);background:#fff;font-size:12px;color:#777;padding:9px 0 0 18px">Email</div>
  <div class="abs" style="left:1005px;top:4658px;width:99px;height:33px;background:var(--blue);color:#fff;font-size:12px;font-weight:700;display:flex;align-items:center;justify-content:center">SUBSCRIBE</div>

  <div class="abs" style="left:113px;top:4770px;width:991px;height:1px;background:var(--line)"></div>
  <div class="abs" style="left:0;top:4797px;width:1200px;text-align:center;font-size:12px;color:var(--blue)">Calloway Pool Service</div>

</div>
</body>
</html>
```